Mortgage Specialist Wordpress Build

I have a current WordPress site but I would like a whole new site built using the same domain. I've included a site for reference in my outline. The main focus of the website is to educate and capture leads.
I would like my blogs to stay for SEO already earned. Please see work requested attached.
Updates
Project Deadline Extended Reason: I am extending the deadline because I didn't realize this was a design only and I need the website coded as well. I've purchased the add-on. This is my first time using Pixel Bazaar so please bare with me. I have additional Wordpress sites I want to have built too. Thanks, Colin Added Tuesday, April 18, 2017
Target Market(s)
Home Buyers, Home owners looking to refinance or renew their mortgages
Industry/Entity Type
Mortgage
Coding
Coded - Design and coding required
Font styles to use
Look and feel
Each slider illustrates characteristics of the customer's brand and the style your logo design should communicate.

```html
<!DOCTYPE html>
<html lang="en">
<head>
<meta charset="utf-8">
<title>Harbourline Lending – North Vancouver Mortgage Broker</title>
<link href="https://fonts.googleapis.com/css2?family=Raleway:wght@400;500;600;700&family=Nunito+Sans:wght@400;600;700&family=Oswald:wght@500&display=swap" rel="stylesheet">
<style>
:root{
  --navy:#163b78;
  --blue:#1e4a99;
  --yellow:#ecc726;
  --yellow-soft:#f6e7a9;
  --grey-text:#8a8a8a;
  --dark:#2a2a2a;
  --body:#666;
  --light-bg:#f2f2f2;
  --news-bg:#eef0f4;
  --white:#fff;
}
*{margin:0;padding:0;box-sizing:border-box}
html,body{width:1200px;height:3010px;overflow:hidden}
body{font-family:"Raleway",sans-serif;color:var(--dark);background:var(--white);position:relative}
section,header,footer{position:absolute;left:0;width:1200px}
.abs{position:absolute}

/* header */
.site-header{top:0;height:110px;background:var(--white)}
.brand{left:76px;top:36px;font-family:"Raleway",sans-serif;font-weight:700;font-size:20px;color:var(--navy);display:flex;align-items:center;gap:10px}
.brand-mark{width:22px;height:22px;background:var(--yellow)}
.main-nav{right:70px;top:38px;display:flex;gap:0}
.main-nav a{display:block;height:40px;line-height:40px;padding:0 26px;font-size:14px;font-weight:600;color:#333;text-decoration:none;margin-left:12px}
.main-nav a.active{background:var(--yellow);color:var(--dark);padding:0 22px}

/* hero */
.hero{top:110px;height:560px;overflow:hidden}
.hero-photo{position:absolute;inset:0;background:linear-gradient(100deg,#3b3a36 0%,#6b6458 35%,#8b8172 55%,#5d574f 80%,#8d8679 100%)}
.hero-photo::after{content:"";position:absolute;inset:0;background:rgba(20,20,20,.35)}
.play{left:550px;top:130px;width:100px;height:100px}
.hero-title{top:236px;width:1200px;text-align:center;font-family:"Nunito Sans",sans-serif;font-weight:700;font-size:39px;color:var(--white)}
.hero-sub{top:294px;width:1200px;text-align:center;font-family:"Nunito Sans",sans-serif;font-weight:400;font-size:32px;color:var(--white)}
.btn{display:block;text-align:center;font-family:"Nunito Sans",sans-serif;font-size:19px;text-decoration:none}
.btn-hook{left:350px;top:374px;width:232px;height:52px;line-height:52px;background:var(--yellow);color:var(--white)}
.btn-client{left:600px;top:374px;width:230px;height:52px;line-height:48px;border:2px solid var(--yellow);color:var(--white)}

/* partners */
.partners{top:670px;height:255px;background:var(--light-bg)}
.partners h2{position:absolute;top:46px;width:1200px;text-align:center;font-family:"Nunito Sans",sans-serif;font-size:28px;font-weight:700;color:var(--navy)}
.partner{top:118px;height:80px;background:#c9c9c9}
.arrow{top:140px;width:20px;height:30px}

/* help */
.help{top:925px;height:525px}
.help h2{position:absolute;top:45px;width:1200px;text-align:center;font-size:34px;font-weight:600;color:var(--grey-text)}
.service{width:314px;height:314px;border:3px solid var(--navy);border-radius:50%;top:135px;background:var(--white);text-align:center}
.service svg{margin-top:62px}
.service h3{font-family:"Nunito Sans",sans-serif;font-weight:400;font-size:28px;color:var(--navy);margin-top:12px}
.pill{display:inline-block;margin-top:10px;padding:0 24px;height:36px;line-height:36px;border-radius:18px;background:var(--yellow-soft);color:var(--navy);font-family:"Nunito Sans",sans-serif;font-size:17px}
.shadow{top:458px;width:220px;height:16px;border-radius:50%;background:radial-gradient(ellipse,rgba(0,0,0,.18),rgba(0,0,0,0) 70%)}

/* search */
.search{top:1450px;height:280px;overflow:hidden}
.search-photo{position:absolute;inset:0;background:linear-gradient(90deg,#7d7269 0%,#a49a93 40%,#4a4a52 75%,#2f3036 100%)}
.search-photo::after{content:"";position:absolute;inset:0;background:rgba(30,30,40,.35)}
.search h2{position:absolute;top:62px;width:1200px;text-align:center;font-size:32px;font-weight:700;color:var(--white)}
.search-input{left:235px;top:150px;width:565px;height:52px;background:var(--white);display:flex;align-items:center;padding-left:22px;gap:14px;font-size:14px;color:#999}
.search-btn{left:815px;top:150px;width:150px;height:52px;line-height:52px;background:var(--yellow);color:var(--white);text-align:center;font-weight:700;font-size:17px}

/* faq */
.faq{top:1730px;height:345px}
.faq h2{position:absolute;left:72px;top:50px;font-size:34px;font-weight:600;color:var(--grey-text)}
.view-all{left:972px;top:50px;width:154px;height:46px;line-height:42px;border:2px solid var(--navy);text-align:center;font-size:13px;font-weight:700;color:var(--navy)}
.faq-item{top:125px;width:330px}
.faq-item h3{font-size:21px;font-weight:500;line-height:28px;color:var(--dark)}
.faq-item p{margin-top:10px;font-size:14px;line-height:23px;color:var(--body)}

/* broker */
.broker{top:2075px;height:430px;overflow:hidden}
.broker-bg{position:absolute;inset:0;background:linear-gradient(180deg,#edcb2d 0%,#e8c730 60%,#d9ba33 100%)}
.portrait{left:80px;top:72px;width:296px;height:296px;border-radius:50%;border:5px solid var(--white);background:radial-gradient(circle at 50% 40%,#d8b8a2 0%,#9b7e6c 40%,#3b3f48 80%)}
.broker h2{position:absolute;left:422px;top:58px;font-family:"Oswald",sans-serif;font-weight:500;font-size:36px;color:var(--dark);letter-spacing:.5px}
.broker p{position:absolute;left:422px;width:690px;font-size:12.5px;line-height:22px;color:var(--dark)}
.btn-read{left:420px;top:325px;width:114px;height:38px;line-height:38px;background:#2d2d2d;color:var(--white);font-size:14px;text-align:center}
.btn-app{left:546px;top:325px;width:180px;height:38px;background:var(--blue);color:var(--white);font-size:14px;display:flex;align-items:center;justify-content:center;gap:8px}

/* newsletter */
.newsletter{top:2505px;height:220px;background:var(--news-bg)}
.newsletter h2{position:absolute;top:38px;width:1200px;text-align:center;font-size:34px;font-weight:600;color:var(--grey-text)}
.news-input{left:316px;top:102px;width:390px;height:52px;line-height:52px;background:var(--white);padding-left:16px;font-size:14px;color:#888}
.news-btn{left:712px;top:102px;width:170px;height:52px;line-height:52px;background:var(--yellow);color:var(--white);text-align:center;font-weight:700;font-size:17px}

/* footer */
.site-footer{top:2725px;height:285px;background:var(--white)}
.footer-brand{left:76px;top:55px}
.copyright{left:76px;top:162px;font-size:13px;line-height:21px;color:var(--body)}
.footer-col h4{font-size:13px;font-weight:700;color:var(--navy);letter-spacing:.5px;margin-bottom:14px}
.footer-col li{list-style:none;font-size:13px;color:var(--body);line-height:32px;display:flex;align-items:center;gap:14px}
.contact-addr{font-size:13px;line-height:22px;color:var(--body);margin-bottom:8px}
.socials{display:flex;gap:8px}
.socials span{width:28px;height:28px;display:block}
</style>
</head>
<body>

<header class="site-header">
  <div class="abs brand"><span class="brand-mark"></span>Harbourline Lending</div>
  <nav class="abs main-nav">
    <a class="active" href="#">HOME</a>
    <a href="#">ABOUT US</a>
    <a href="#">BLOG</a>
    <a href="#">CONTACT US</a>
  </nav>
</header>

<section class="hero">
  <div class="hero-photo" role="img" aria-label="Photo of a couple meeting with a mortgage broker at a laptop"></div>
  <svg class="abs play" viewBox="0 0 100 100"><circle cx="50" cy="50" r="47" fill="none" stroke="#fff" stroke-width="3"/><path d="M40 32 L68 50 L40 68 Z" fill="none" stroke="#fff" stroke-width="3" stroke-linejoin="round"/></svg>
  <h1 class="abs hero-title">Class aptent taciti sociosqu litora torquent</h1>
  <p class="abs hero-sub">Aonubia nostra inceptos hymenaeos</p>
  <a class="abs btn btn-hook" href="#">Get Hooked Up</a>
  <a class="abs btn btn-client" href="#">I'm a Client</a>
</section>

<section class="partners">
  <h2>Some Of My Lending Partners</h2>
  <svg class="abs arrow" style="left:72px" viewBox="0 0 20 30"><path d="M14 6 L6 15 L14 24" fill="none" stroke="#888" stroke-width="2.5"/></svg>
  <div class="abs partner" style="left:130px;width:110px;border-radius:6px"></div>
  <div class="abs partner" style="left:300px;width:80px"></div>
  <div class="abs partner" style="left:445px;width:110px"></div>
  <div class="abs partner" style="left:620px;width:120px;height:40px;top:138px"></div>
  <div class="abs partner" style="left:798px;width:108px;border-radius:4px"></div>
  <div class="abs partner" style="left:972px;width:78px"></div>
  <svg class="abs arrow" style="left:1108px" viewBox="0 0 20 30"><path d="M6 6 L14 15 L6 24" fill="none" stroke="#888" stroke-width="2.5"/></svg>
</section>

<section class="help">
  <h2>I need help with</h2>
  <div class="abs service" style="left:80px">
    <svg width="110" height="80" viewBox="0 0 110 80" fill="none" stroke="#163b78" stroke-width="3.5" stroke-linejoin="round">
      <path d="M5 8 H20 L32 52 H92 L102 20 H24"/><path d="M40 30 H96 M36 41 H94 M50 20 V52 M66 20 V52 M82 20 V52"/>
      <circle cx="42" cy="68" r="7"/><circle cx="82" cy="68" r="7"/></svg>
    <h3>Purchase</h3><span class="pill">Click here</span>
  </div>
  <div class="abs shadow" style="left:127px"></div>
  <div class="abs service" style="left:443px">
    <svg width="90" height="80" viewBox="0 0 90 80" fill="none" stroke="#163b78" stroke-width="3.5">
      <path d="M14 46 A32 32 0 0 1 66 14"/><path d="M60 6 L68 14 L58 20"/>
      <path d="M76 34 A32 32 0 0 1 24 66"/><path d="M30 74 L22 66 L32 60"/>
      <path d="M53 28 C50 24 36 24 36 32 C36 40 54 38 54 47 C54 55 40 56 36 51 M45 20 V60"/></svg>
    <h3>Refinance</h3><span class="pill">Click here</span>
  </div>
  <div class="abs shadow" style="left:490px"></div>
  <div class="abs service" style="left:803px">
    <svg width="90" height="80" viewBox="0 0 90 80" fill="none" stroke="#163b78" stroke-width="3.5" stroke-linejoin="round">
      <path d="M10 40 L22 22 H70 L62 12 M70 22 L62 32"/>
      <path d="M80 40 L68 58 H20 L28 68 M20 58 L28 48"/></svg>
    <h3>Renew</h3><span class="pill">Click here</span>
  </div>
  <div class="abs shadow" style="left:850px"></div>
</section>

<section class="search">
  <div class="search-photo" role="img" aria-label="Photo of a hand typing on a laptop keyboard"></div>
  <h2>Mortgage or Real Estate Questions?</h2>
  <div class="abs search-input">
    <svg width="16" height="16" viewBox="0 0 16 16" fill="none" stroke="#555" stroke-width="2"><circle cx="6.5" cy="6.5" r="4.5"/><path d="M10 10 L14 14"/></svg>
    Search our data base
  </div>
  <div class="abs search-btn">SEARCH</div>
</section>

<section class="faq">
  <h2>FAQ's</h2>
  <div class="abs view-all">VIEW ALL</div>
  <article class="abs faq-item" style="left:75px">
    <h3>Nam fermentum vestibulum purus id aliquet.?</h3>
    <p>Duis aliquam nibh a dui iaculis viverra id a velit. Vivamus egestas risus in magna varius commodo. Sed semper viverra egestas. Etiam pretium porttitor lectus</p>
  </article>
  <article class="abs faq-item" style="left:433px">
    <h3>Nam fermentum vestibulum purus id aliquet.?</h3>
    <p>Duis aliquam nibh a dui iaculis viverra id a velit. Vivamus egestas risus in magna varius commodo. Sed semper viverra egestas. Etiam pretium porttitor lectus</p>
  </article>
  <article class="abs faq-item" style="left:790px">
    <h3>Nam fermentum vestibulum purus id aliquet.?</h3>
    <p>Duis aliquam nibh a dui iaculis viverra id a velit. Vivamus egestas risus in magna varius commodo. Sed semper viverra egestas. Etiam pretium porttitor lectus</p>
  </article>
</section>

<section class="broker">
  <div class="broker-bg"></div>
  <div class="abs portrait" role="img" aria-label="Portrait photo of the mortgage broker"></div>
  <h2>NORTH VANCOUVER MORTGAGE BROKER</h2>
  <p style="top:128px">Purchasing a home, refinancing a mortgage and renewing a mortgage have one thing in common: they can represent an exciting time in an individual's life but they can also be complex. I am dedicated to giving back to the region by helping people save thousands of dollars in interest and prepayment expenses and find solutions that are fitted to your specific situation.</p>
  <p style="top:218px">In addition to getting you a fantastic rate, I ensure that I take enough time for each and every one of my clients to go over every detail in order to see that their mortgage repayment schedule is on track with their financial objectives. It is my mission to help people in this wonderful area get the best North Vancouver mortgage package possible while providing tremendous care and service.</p>
  <div class="abs btn-read">Read More</div>
  <div class="abs btn-app">
    <svg width="14" height="14" viewBox="0 0 14 14" fill="#fff"><path d="M5 1 H9 V6 H12 L7 11 L2 6 H5 Z"/><rect x="1" y="12" width="12" height="2"/></svg>
    Download My App
  </div>
</section>

<section class="newsletter">
  <h2>Sign up Newsletter</h2>
  <div class="abs news-input">Enter Email Address</div>
  <div class="abs news-btn">SIGN UP</div>
</section>

<footer class="site-footer">
  <div class="abs brand footer-brand"><span class="brand-mark"></span>Harbourline Lending</div>
  <div class="abs copyright">© 2017 Colin Ashford<br>Keystone Mortgage Group. All Rights Reserved.<br>Privacy &amp; Content Notice</div>
  <div class="abs footer-col" style="left:432px;top:52px">
    <h4>SITE MAP</h4>
    <ul><li>Home</li><li>About</li><li>Blog</li><li>Contact Us</li></ul>
  </div>
  <div class="abs footer-col" style="left:632px;top:52px">
    <h4>CONTACT ADDRESS</h4>
    <p class="contact-addr">415 Harbour Ave.<br>North Vancouver, BC V7M 0A4</p>
    <ul>
      <li><svg width="12" height="12" viewBox="0 0 12 12" fill="#163b78"><path d="M2 1 L4.5 1 L5.5 4 L4 5 C5 7 6 8 7.5 8.5 L8.5 7 L11 8 L11 10.5 C6 11 1 6 2 1Z"/></svg>604.555.0142</li>
      <li><svg width="12" height="12" viewBox="0 0 12 12" fill="#163b78"><rect x="1" y="4" width="10" height="7"/><rect x="3" y="1" width="6" height="3"/></svg>604.555.0187</li>
      <li><svg width="12" height="12" viewBox="0 0 12 12" fill="#163b78"><path d="M0 2 H12 V10 H0 Z M0 2 L6 7 L12 2" stroke="#fff" stroke-width=".8"/></svg>colin@keystonemortgage.ca</li>
    </ul>
  </div>
  <div class="abs footer-col" style="left:908px;top:52px">
    <h4>FOLLOW US</h4>
    <div class="socials">
      <span style="background:#3b5a9a"></span><span style="background:#4c79a3"></span><span style="background:#2aa3ef"></span><span style="background:#dc4a38"></span><span style="background:#0f76b0"></span><span style="background:#e02a20;border-radius:6px"></span>
    </div>
  </div>
</footer>

</body>
</html>
```